Premium Skincare Packaging Design for Vale Hollow

Vale Hollow (https://valehollowgoods.com) is a premium wellness brand from Canada specializing in beef tallow (for cooking) and now expanding into natural skincare. We are seeking packaging design concepts for two new 60 ml skincare products made with grass-fed beef tallow.
Our goal is to achieve a clean, minimalist yet luxurious look that reflects purity, quality and sophistication. The design should look premium enough for high-end skincare shelves while maintaining a natural, grounded feel.
You will be designing:
- Jar label (wrap-around design) for a 60 ml glass jar with black lid
- Round lid sticker (for the top of the black lid)
- Square outer box (for each jar)
- Both products are very similar, so the differentiation can be minimal.

Products to Design
1. Everyday Suet Salve
Jar: Frosted glass, 60 ml with black lid
Purpose: Moisturizer for face, lips, hands, and body
Ingredients: Grass-fed beef tallow, beeswax, honey, vitamin E
Tone: Natural, pure, versatile, gentle
Tagline: “Crafted from nature’s simplest elements”
Preferred color palette:
Light / off-white background
Beige and honey accents
Black or dark brown typography
Mood: Minimalist apothecary meets warm, natural simplicity
2. Visage Suet Lotion
Purpose: Face moisturizer with nourishing tallow and botanicals
Tone: Refined, elegant, modern, premium
Tagline: “The strength of tallow, refined for your face”
Preferred color palette:
Deep charcoal or black background
Gold or cream typography
Accent in subtle metallic tones (gold or bronze)
Mood: Modern luxury with understated confidence
Design Deliverables
For each product, submit:
1) Jar Label (Wrap-around)
- Include product name, logo, tagline, ingredients, and size (60 ml / 2 fl oz).
- Space for barcode and manufacturing details (leave placeholder).
2) Round Lid Sticker
- Centered logo and minimalist border or accent ring.
3) Outer Paper Box (Square)
- Matching color palette and typography.
- Clean layout featuring the Vale Hollow logo and tagline.
- Text to include: product name, tagline, ingredients and size.

Brand Guidelines
Logo: Use the existing Vale Hollow logo (we’ll upload it for reference).
Typography: Clean and elegant — sans-serif or classic serif fonts.
Tone: Pure, premium, and intentional — less is more.
Design cohesion: Both products must look like part of one collection.

```html
<!DOCTYPE html>
<html lang="en">
<head>
<meta charset="utf-8">
<title>Vale Hollow — Everyday Suet Salve Packaging</title>
<link rel="stylesheet" href="https://fonts.googleapis.com/css2?family=Montserrat:wght@500&family=Barlow+Condensed:ital,wght@0,400;0,500;1,500&family=Roboto+Condensed:wght@400;700&display=swap">
<style>
  :root {
    --backdrop: #e3e3e3;
    --ink: #0b0b0b;
    --paper: #ececec;
    --paper-light: #f4f4f4;
    --white: #ffffff;
    --gold: #d2a829;
    --gold-deep: #c8902f;
    --rule: #c9a46a;
    --text-dark: #151515;
  }
  * { box-sizing: border-box; margin: 0; padding: 0; }
  html, body {
    width: 1200px; height: 849px; overflow: hidden;
    background: var(--backdrop);
  }
  .canvas { position: relative; width: 1200px; height: 849px; }

  .brand-name {
    font-family: "Montserrat", sans-serif;
    font-weight: 500;
    color: var(--white);
    text-transform: uppercase;
    letter-spacing: 0.12em;
    white-space: nowrap;
  }

  /* Outer box front panel */
  .box-face {
    position: absolute; left: 80px; top: 185px;
    width: 480px; height: 480px;
    background: var(--paper-light);
    display: flex; flex-direction: column;
    box-shadow: 0 18px 40px rgba(0,0,0,0.12);
  }
  .box-face .band-dark {
    height: 265px; background: var(--ink);
    display: flex; align-items: flex-end; justify-content: center;
    padding-bottom: 42px;
  }
  .box-face .brand-name { font-size: 40px; }
  .box-face .box-copy {
    flex: 1; display: flex; flex-direction: column; align-items: center;
    padding-top: 34px; gap: 8px;
    font-family: "Roboto Condensed", sans-serif; color: var(--text-dark);
  }
  .box-copy .tagline { font-size: 22px; }
  .box-copy .product { font-size: 20px; }
  .box-face .band-gold { height: 30px; background: var(--gold); }

  /* Lid sticker */
  .lid-sticker { position: absolute; left: 780px; top: 62px; width: 190px; height: 190px; }
  .lid-sticker .brand-name {
    position: absolute; inset: 0;
    display: flex; align-items: center; justify-content: center;
    font-size: 19px;
  }

  /* Flat jar label */
  .jar-label {
    position: absolute; left: 620px; top: 330px;
    width: 520px; height: 228px;
    background: var(--white);
    display: flex; flex-direction: column;
    box-shadow: 0 10px 26px rgba(0,0,0,0.10);
  }
  .jar-label .band-dark {
    height: 96px; background: var(--ink);
    display: flex; align-items: center; justify-content: center;
  }
  .jar-label .brand-name { font-size: 26px; }
  .jar-label .label-body { flex: 1; position: relative; }
  .side-notes {
    position: absolute; left: 12px; top: 10px; height: 110px;
    display: flex; flex-direction: row-reverse; gap: 6px;
    writing-mode: vertical-rl;
    font-family: "Roboto Condensed", sans-serif; font-size: 8.5px; line-height: 1.25;
    color: var(--text-dark);
  }
  .side-notes strong { font-weight: 700; }
  .side-notes p { max-height: 110px; }
  .label-centre {
    position: absolute; left: 150px; right: 150px; top: 8px;
    display: flex; flex-direction: column; align-items: center;
    color: var(--text-dark);
  }
  .headline {
    font-family: "Barlow Condensed", sans-serif; font-weight: 500;
    font-size: 17px; line-height: 1.1; text-align: center; text-transform: uppercase;
  }
  .rule { width: 100%; height: 1px; background: var(--rule); margin: 6px 0; }
  .product-name {
    font-family: "Barlow Condensed", sans-serif; font-style: italic; font-weight: 500;
    font-size: 12px; letter-spacing: 0.14em; text-transform: uppercase;
  }
  .sizes {
    display: flex; gap: 44px; margin-top: 5px;
    font-family: "Roboto Condensed", sans-serif; font-size: 12px; letter-spacing: 0.06em;
  }
  .jar-label .band-gold {
    height: 10px;
    background: linear-gradient(90deg, var(--gold-deep), var(--gold) 50%, var(--gold-deep));
  }
</style>
</head>
<body>
<main class="canvas">

  <section class="box-face" aria-label="Outer box front panel">
    <div class="band-dark">
      <span class="brand-name">Vale Hollow</span>
    </div>
    <div class="box-copy">
      <p class="tagline">Crafted from nature’s simplest elements</p>
      <p class="product">Everyday Suet Salve</p>
    </div>
    <div class="band-gold"></div>
  </section>

  <section class="lid-sticker" aria-label="Round lid sticker">
    <svg width="190" height="190" viewBox="0 0 190 190" aria-hidden="true">
      <defs>
        <linearGradient id="ring-gold" x1="0" y1="0" x2="1" y2="1">
          <stop offset="0" stop-color="#c8902f"/>
          <stop offset="0.5" stop-color="#e0b64a"/>
          <stop offset="1" stop-color="#c8902f"/>
        </linearGradient>
      </defs>
      <circle cx="95" cy="95" r="94" fill="url(#ring-gold)"/>
      <circle cx="95" cy="95" r="90" fill="#0b0b0b"/>
      <circle cx="95" cy="95" r="86" fill="none" stroke="#c9a46a" stroke-width="0.8"/>
    </svg>
    <span class="brand-name">Vale Hollow</span>
  </section>

  <section class="jar-label" aria-label="Jar wrap-around label">
    <div class="band-dark">
      <span class="brand-name">Vale Hollow</span>
    </div>
    <div class="label-body">
      <div class="side-notes">
        <p>Moisturizer for face, lips,<br>hands, and body</p>
        <p><strong>Ingredients:</strong><br>Grass-fed beef tallow, honey,<br>beeswax, vitamin E</p>
      </div>
      <div class="label-centre">
        <div class="rule"></div>
        <h2 class="headline">Crafted from nature’s<br>simplest elements</h2>
        <div class="rule"></div>
        <p class="product-name">Everyday Suet Salve</p>
        <div class="rule"></div>
        <div class="sizes"><span>60 ml</span><span>2 fl oz</span></div>
      </div>
    </div>
    <div class="band-gold"></div>
  </section>

</main>
</body>
</html>
```